Vacation giveaway landing page design

We are giving away a holiday/vacation to Rome and we need a landing page designed that will entice people to enter their email address for a chance to win!

Full brief, examples and everything else can be found in this document: https://files.quorvanshare.net/page/7-tmzrwpQY4vxkaLn8sbgeXu2fcTo5kWdn3jhpyuBc29m/open?mode=viewing

Number of Pages Required

1 page

```html
<!DOCTYPE html>
<html lang="en">
<head>
<meta charset="utf-8">
<title>The Wanderlots – Prize Draw</title>
<link rel="stylesheet" href="https://fonts.googleapis.com/css2?family=Barlow+Condensed:wght@400;500;600;700&family=Barlow+Semi+Condensed:wght@400;500;700&display=swap">
<style>
:root{
  --ink:#4a4a4a;
  --white:#ffffff;
  --red:#f4313b;
  --navy:#1c6a92;
  --gold:#f5b82e;
  --teal:#2fbaad;
  --link:#1b6fa8;
  --line:#d8d8d8;
}
*{box-sizing:border-box;margin:0;padding:0}
html,body{width:1200px;height:2213px;overflow:hidden;background:var(--white)}
body{position:relative;font-family:"Barlow Semi Condensed",sans-serif;color:var(--ink)}
.abs{position:absolute}
.hero{left:0;top:0;width:1200px;height:1090px;
  background:
   radial-gradient(ellipse 300px 260px at 980px 220px,#a98e86 0%,rgba(169,142,134,0) 70%),
   radial-gradient(ellipse 420px 300px at 180px 360px,rgba(140,160,175,.75) 0%,rgba(140,160,175,0) 70%),
   linear-gradient(180deg,#2a7fa3 0%,#3a87a4 30%,#2f8c96 45%,#1f8c7a 65%,#17955f 85%,#1d8d63 100%);}
.hero-sand{left:0;top:430px;width:360px;height:660px;
  background:linear-gradient(100deg,rgba(215,205,190,.55) 0%,rgba(200,190,170,.25) 60%,rgba(0,0,0,0) 100%)}
.brand{left:112px;top:62px;display:flex;align-items:center;gap:14px;color:var(--white)}
.brand-mark{width:64px;height:64px;border:3px solid var(--white);border-radius:50%}
.brand-name{font-family:"Barlow Condensed",sans-serif;font-weight:700;font-size:44px;line-height:.95;letter-spacing:1px;text-transform:uppercase}
.intro{left:451px;top:50px;width:460px;font-family:"Barlow Condensed",sans-serif;font-size:29px;line-height:39px;color:var(--white)}
.perks{left:451px;top:152px;list-style:none}
.perks li{display:flex;align-items:center;gap:14px;height:50px;font-family:"Barlow Condensed",sans-serif;font-weight:700;font-size:29px;color:var(--white);text-transform:uppercase;letter-spacing:.5px}
.tick{width:26px;height:26px;flex:none}
.btn{display:inline-flex;align-items:center;justify-content:center;background:var(--red);color:var(--white);border-radius:26px;font-family:"Barlow Condensed",sans-serif;font-weight:700;font-size:22px;text-transform:uppercase;height:52px}
.btn-top{left:451px;top:321px;width:183px}
.h-free,.h-draw{top:420px;font-family:"Barlow Condensed",sans-serif;font-size:48px;color:var(--white)}
.h-free{left:111px}
.h-draw{left:676px}
.email{left:111px;top:525px;width:490px;height:58px;background:var(--white);display:flex;align-items:center;gap:9px;padding-left:20px;font-family:"Barlow Condensed",sans-serif;font-size:18px;color:#555}
.consent{left:111px;top:616px;width:500px;display:flex;gap:12px;font-family:"Barlow Condensed",sans-serif;font-size:20px;line-height:33px;color:var(--white)}
.box{width:25px;height:22px;border:2px solid rgba(255,255,255,.8);flex:none;margin-top:6px}
.btn-enter{left:112px;top:753px;width:183px}
.plan{left:674px;font-family:"Barlow Condensed",sans-serif;color:var(--white)}
.plan-title{display:flex;align-items:center;gap:13px;font-size:29px}
.plan-title .box{width:34px;height:30px;margin-top:0;border-color:var(--white)}
.plan-title b{font-weight:700;font-size:31px}
.plan-title small{font-size:22px}
.plan ul{list-style:none;margin-top:12px;padding-left:5px}
.plan li{display:flex;align-items:center;gap:12px;height:36px;font-weight:700;font-size:22px}
.plan li .tick{width:19px;height:19px}
.plan-a{top:522px}
.plan-b{top:754px}
.btn-checkout{left:679px;top:948px;width:183px}
.winners-title{left:0;top:1176px;width:1200px;text-align:center;font-family:"Barlow Condensed",sans-serif;font-weight:700;font-size:45px;color:var(--navy)}
.rule{left:542px;top:1249px;width:116px;height:6px;background:var(--navy)}
.card{top:1320px;width:307px;height:420px;border:1px solid var(--line);background:var(--white)}
.card-photo{height:203px;width:100%}
.card-body{padding:18px 18px 0;font-size:13.5px;line-height:24px;color:#444}
.card-body a{color:var(--link);text-decoration:none}
.card-meta{position:absolute;left:18px;bottom:14px;display:flex;gap:30px;font-size:13.5px;color:#777}
.caption{top:1772px;width:307px;text-align:center;font-family:"Barlow Condensed",sans-serif;font-weight:700;font-size:21px;line-height:32px;color:#4a4a4a;text-transform:uppercase}
.caption .prize{color:var(--navy)}
.caption .prize span{color:var(--gold)}
.footer{left:0;top:1958px;width:1200px;height:255px;background:var(--teal);color:var(--white);font-family:"Barlow Condensed",sans-serif}
.f-contact{left:111px;top:52px}
.f-contact h3{font-weight:700;font-size:25px;text-transform:uppercase}
.f-contact p{font-size:22px;display:flex;align-items:center;gap:6px;margin-top:6px}
.f-links{left:522px;top:52px;font-weight:700;font-size:25px;line-height:38px}
.cards{left:855px;top:62px;display:flex;gap:12px}
.pay{width:71px;height:46px;background:var(--white);border-radius:4px;display:flex;align-items:center;justify-content:center;font-family:"Barlow Condensed",sans-serif;font-weight:700;font-size:15px;color:var(--navy)}
.legal{left:0;top:164px;width:1200px;text-align:center;font-size:16px;line-height:31px}
</style>
</head>
<body>

<section class="abs hero" role="img" aria-label="Photo of a Mediterranean coastal town with a beach, turquoise sea and a large rock headland"></section>
<div class="abs hero-sand"></div>

<div class="abs brand">
  <span class="brand-mark"></span>
  <span class="brand-name">The<br>Wanderlots</span>
</div>

<p class="abs intro">As you'll see, it's a paid for service which gets you three things:</p>
<ul class="abs perks">
  <li><svg class="tick" viewBox="0 0 26 26"><circle cx="13" cy="13" r="13" fill="#fff"/><path d="M7 13.5l4 4 8-8" stroke="#2a7fa3" stroke-width="3" fill="none"/></svg>Monthly entry into a prize draw</li>
  <li><svg class="tick" viewBox="0 0 26 26"><circle cx="13" cy="13" r="13" fill="#fff"/><path d="M7 13.5l4 4 8-8" stroke="#2a7fa3" stroke-width="3" fill="none"/></svg>Weekly discount emails</li>
  <li><svg class="tick" viewBox="0 0 26 26"><circle cx="13" cy="13" r="13" fill="#fff"/><path d="M7 13.5l4 4 8-8" stroke="#2a7fa3" stroke-width="3" fill="none"/></svg>Monthly digital magazine</li>
</ul>
<a class="abs btn btn-top">Get it all now</a>

<h2 class="abs h-free">Free Entry into a prize draw</h2>
<h2 class="abs h-draw">Prize draw</h2>

<div class="abs email">
  <svg width="18" height="14" viewBox="0 0 18 14"><rect width="18" height="14" rx="1" fill="#666"/><path d="M1 1l8 6 8-6" stroke="#fff" stroke-width="1.5" fill="none"/></svg>
  Email Address
</div>
<div class="abs consent">
  <span class="box"></span>
  <p>By entering your email address, you agree to receive updates about the competition and The Wanderlots. You can review our competition terms and conditions here.</p>
</div>
<a class="abs btn btn-enter">Enter now!</a>

<div class="abs plan plan-a">
  <div class="plan-title"><span class="box"></span>15 Entries &amp; weekly deals : <b>£4.99</b><small>per month</small></div>
  <ul>
    <li><svg class="tick" viewBox="0 0 26 26"><circle cx="13" cy="13" r="13" fill="#fff"/><path d="M7 13.5l4 4 8-8" stroke="#1f8c7a" stroke-width="3.5" fill="none"/></svg>Weekly Deals Email (?)</li>
    <li><svg class="tick" viewBox="0 0 26 26"><circle cx="13" cy="13" r="13" fill="#fff"/><path d="M7 13.5l4 4 8-8" stroke="#1f8c7a" stroke-width="3.5" fill="none"/></svg>Save £100's on Holidays (?)</li>
    <li><svg class="tick" viewBox="0 0 26 26"><circle cx="13" cy="13" r="13" fill="#fff"/><path d="M7 13.5l4 4 8-8" stroke="#1f8c7a" stroke-width="3.5" fill="none"/></svg>Monthly Magazine (?)</li>
    <li><svg class="tick" viewBox="0 0 26 26"><circle cx="13" cy="13" r="13" fill="#fff"/><path d="M7 13.5l4 4 8-8" stroke="#1f8c7a" stroke-width="3.5" fill="none"/></svg>15 Entries Every Month</li>
  </ul>
</div>
<div class="abs plan plan-b">
  <div class="plan-title"><span class="box"></span>1 Entry : <b>£2.99</b><small>per month</small></div>
  <ul>
    <li><svg class="tick" viewBox="0 0 26 26"><circle cx="13" cy="13" r="13" fill="#fff"/><path d="M7 13.5l4 4 8-8" stroke="#17955f" stroke-width="3.5" fill="none"/></svg>Save £100's on Holidays (?)</li>
    <li><svg class="tick" viewBox="0 0 26 26"><circle cx="13" cy="13" r="13" fill="#fff"/><path d="M7 13.5l4 4 8-8" stroke="#17955f" stroke-width="3.5" fill="none"/></svg>Monthly Magazine (?)</li>
    <li><svg class="tick" viewBox="0 0 26 26"><circle cx="13" cy="13" r="13" fill="#fff"/><path d="M7 13.5l4 4 8-8" stroke="#17955f" stroke-width="3.5" fill="none"/></svg>1 Entry Every Month</li>
  </ul>
</div>
<a class="abs btn btn-checkout">Go to checkout</a>

<h2 class="abs winners-title">PREVIOUS WINNERS</h2>
<div class="abs rule"></div>

<article class="abs card" style="left:112px">
  <div class="card-photo" role="img" aria-label="Winner photo in a busy city square" style="background:linear-gradient(135deg,#a49a88,#4c4a4c 60%,#2c2a2e)"></div>
  <div class="card-body">Nadia Rahman is the lucky winner this month!<br>She's off to see the incredible Northern Lights in Iceland!<br>Next month's prize? Flights to New York City!<br>Enter to win here - <a>https://wndr.example/ny19</a></div>
  <div class="card-meta"><span>👍 12</span><span>💬 Comment</span><span>↪ 2</span></div>
</article>
<article class="abs card" style="left:447px">
  <div class="card-photo" role="img" aria-label="Winner selfie photo" style="background:linear-gradient(135deg,#e8b98f,#c98f6a 55%,#3a2a28)"></div>
  <div class="card-body">This month's winner, Lucy Hartley, is escaping to the Greek islands for a week long getaway!<br>Next month's giveaway: 7 nights on the beautiful coast of Portugal. Enter now<br><a>http://wndr.example/pt19</a></div>
  <div class="card-meta"><span>👍 12</span><span>💬 Comment</span><span>↪ 2</span></div>
</article>
<article class="abs card" style="left:781px">
  <div class="card-photo" role="img" aria-label="Winner photo in a green park" style="background:linear-gradient(135deg,#6f8f4e,#3d5a2c 60%,#2a2422)"></div>
  <div class="card-body">Congratulations to this month's winner Carla Benson - she has won a week long holiday in B-E-A-UTIFUL Portugal!<br>Next month you could win 7 nights in the Canary Islands! Get signed up here -<br><a>http://wndr.example/cn19</a></div>
  <div class="card-meta"><span>👍 12</span><span>💬 Comment</span><span>↪ 2</span></div>
</article>

<div class="abs caption" style="left:112px">January's winner<br>Prize:<br><span class="prize">A <span>Northern Lights</span> getaway</span></div>
<div class="abs caption" style="left:447px">March's winner<br>Prize:<br><span class="prize">A week in <span>the Greek Islands</span></span></div>
<div class="abs caption" style="left:781px">April's winner<br>Prize:<br><span class="prize">A week in <span>Portugal</span></span></div>

<footer class="abs footer">
  <div class="abs f-contact">
    <h3>Contact</h3>
    <p><svg width="20" height="15" viewBox="0 0 18 14"><rect width="18" height="14" rx="1" fill="#fff"/><path d="M1 1l8 6 8-6" stroke="#2fbaad" stroke-width="1.5" fill="none"/></svg>info@wanderlotsclub.example</p>
  </div>
  <div class="abs f-links">Terms &amp; Conditions<br>Privacy Policy</div>
  <div class="abs cards">
    <span class="pay">Cardly</span><span class="pay">Orbit Pay</span><span class="pay">Nexa</span>
  </div>
  <p class="abs legal">© 2019 Harbourline Ltd a private limited company registered in England and Wales, Reg No: 10482215.<br>Reg office and postal address: 12 Marlow Quay Road, London, SE1 4ZZ, UK</p>
</footer>

</body>
</html>
```